Marlow Ridgeway a PlateWork Fabricator! Pressure Vessels, Stainless Vessels, Steel Fabricator!

Update and modernize the www.marlowridgeway.example website. Basically throwing away the old site and coming back with a new feel, new look, but some of the same content. One of our other companies is www.keltonbuilders.example and if you view that site you will get a idea of how we would like the site to feel. Below are the MR logos and the colors are #231F20 and #6D0B17 and the font is Ethnocentric Rg.

Target Market(s)

Steel Fabrication, Platework, Vessel Fabrication,

Industry/Entity Type

Steel

Coding

Coded - Design and coding required

Number of Pages Required

5+ page

Font styles to use
Other font styles liked:
• Ethnocentric Rg

Requirements
Must have
• Industry feel... site must flow and color scheme and font be consistent.

```html
<!DOCTYPE html>
<html lang="en">
<head>
<meta charset="utf-8">
<title>Marlow Ridgeway — Fabrication Services</title>
<link href="https://fonts.googleapis.com/css2?family=Orbitron:wght@600;800&family=Barlow+Condensed:wght@400;500;600&family=Barlow:wght@400;500&display=swap" rel="stylesheet">
<style>
:root{
  --ink:#231F20;
  --dark:#1f2025;
  --panel:#2a2b31;
  --panel-2:#26272c;
  --brand:#6D0B17;
  --brand-bright:#8e1a25;
  --quote-red:#9a2029;
  --text:#d9d9dc;
  --muted:#9a9ba2;
  --white:#ffffff;
  --line:rgba(255,255,255,.28);
}
*{box-sizing:border-box;margin:0;padding:0}
html,body{width:1200px;height:3764px;overflow:hidden}
body{background:var(--dark);color:var(--text);font-family:"Barlow",sans-serif;position:relative}
.display{font-family:"Orbitron",sans-serif;font-weight:800;text-transform:uppercase;letter-spacing:3px;color:var(--white)}
.eyebrow{font-family:"Barlow Condensed",sans-serif;font-size:14px;letter-spacing:1.5px;text-transform:uppercase;color:var(--muted)}
.btn{display:inline-flex;align-items:center;gap:14px;height:34px;padding:0 18px;font-family:"Barlow Condensed",sans-serif;font-weight:600;font-size:14px;letter-spacing:1px;text-transform:uppercase;color:var(--white);text-decoration:none;clip-path:polygon(0 0,100% 0,92% 100%,0 100%);padding-right:28px}
.btn-red{background:var(--brand)}
.btn-light{background:transparent;border:1px solid var(--line)}
.arrow{width:14px;height:8px}
.photo{position:absolute}

/* header */
.hero{position:absolute;left:0;top:0;width:1200px;height:610px;background:linear-gradient(90deg,#3a3b40 0%,#55575c 45%,#6e7075 70%,#2e2f33 100%)}
.hero .photo{inset:0;background:radial-gradient(ellipse at 70% 40%,rgba(200,202,206,.45),transparent 60%),linear-gradient(180deg,rgba(0,0,0,.1),rgba(20,20,24,.7))}
.nav{position:absolute;top:40px;left:60px;right:60px;display:flex;align-items:center}
.brand{display:flex;align-items:center;gap:10px;font-family:"Orbitron",sans-serif;font-weight:800;font-size:18px;color:var(--white);text-transform:uppercase;letter-spacing:1px}
.brand .mark{width:30px;height:30px;border:2px solid var(--white);border-radius:50%}
.menu{display:flex;gap:34px;margin-left:auto;margin-right:40px;list-style:none;font-family:"Barlow Condensed",sans-serif;font-size:15px;color:var(--white)}
.menu li.active{border-bottom:2px solid var(--brand);padding-bottom:4px}
.hero-copy{position:absolute;left:60px;top:250px}
.hero-copy .lead{font-family:"Barlow Condensed",sans-serif;font-size:28px;color:var(--white);margin-bottom:14px}
.hero-copy h1{font-size:46px;letter-spacing:6px}
.hero-copy .phone{font-family:"Barlow Condensed",sans-serif;font-size:14px;color:var(--white);margin:22px 0 26px}
.slider{position:absolute;right:60px;top:268px;display:flex;flex-direction:column;gap:12px}
.slider span{width:28px;height:28px;border-radius:50%;background:var(--brand);display:block}
.slider span+span{background:var(--white)}

/* quality */
.quality{position:absolute;top:610px;left:0;width:1200px;height:620px;background:var(--panel)}
.quality .heading{text-align:center;padding-top:112px}
.quality h2{font-size:30px;line-height:1.35;margin-top:8px}
.pipes{left:0;top:220px;width:540px;height:380px;background:radial-gradient(ellipse at 40% 50%,#cfd1d4,#7d7f84 45%,transparent 72%)}
.quality .content{position:absolute;left:560px;top:240px;width:520px}
.badges{display:flex;gap:30px;align-items:center;margin-bottom:56px}
.badges span{display:block;width:70px;height:46px;background:#4a4b51}
.badges span.round{border-radius:50%;width:56px;height:56px}
.quality p{font-size:15px;line-height:1.65;color:var(--text);margin-bottom:34px}
.actions{display:flex;gap:20px}

/* divider */
.divider{position:absolute;top:1230px;left:0;width:1200px;height:42px;background:#35363c;border-top:1px solid #45464c;border-bottom:1px solid #45464c}

/* success */
.success{position:absolute;top:1272px;left:0;width:1200px;height:608px;background:var(--panel-2)}
.success .photo{left:380px;top:80px;width:480px;height:440px;background:radial-gradient(ellipse at center,#55565b,transparent 70%)}
.success .copy{position:absolute;left:180px;top:200px;width:840px}
.success h2{font-size:30px;margin:10px 0 26px}
.cols{display:flex;gap:40px;font-size:14px;line-height:1.6}
.cols p{flex:1}
.success .btn{position:absolute;right:0;top:226px}

/* testimonials */
.reviews{position:absolute;top:1880px;left:0;width:1200px;height:900px;background:var(--panel-2)}
.reviews .photo{left:480px;top:400px;width:720px;height:500px;background:linear-gradient(180deg,#c9c6c2 0%,#a9a6a4 55%,#2b2c31 100%);clip-path:polygon(0 56%,100% 0,100% 100%,0 100%)}
.reviews .copy{position:absolute;left:180px;top:130px;width:780px}
.reviews h2{font-size:28px;line-height:1.4;margin:10px 0 34px;max-width:600px}
.quote-mark{font-family:"Orbitron",sans-serif;color:var(--brand-bright);font-size:40px;line-height:1}
.reviews blockquote{font-size:15px;line-height:1.65;margin:0 0 0 40px;width:700px;color:var(--text)}
.reviews .close-mark{margin:4px 0 0 250px}
.reviews .actions{margin-top:40px}

/* quote form */
.quote{position:absolute;left:180px;top:2770px;width:840px;height:650px;background:var(--quote-red);padding:70px 50px}
.quote h2{font-size:28px;margin:8px 0 36px}
.quote .eyebrow{color:#e5b7bb}
.row{display:flex;gap:20px;margin-bottom:22px}
.field{flex:1;display:flex;flex-direction:column;gap:6px}
.field label{font-family:"Barlow Condensed",sans-serif;font-size:13px;letter-spacing:1px;text-transform:uppercase;color:var(--white)}
.field .input{height:38px;border:1px solid rgba(255,255,255,.55);font-size:13px;color:#eac8cb;padding:10px 12px}
.field .area{height:160px}
.quote .submit{display:flex;justify-content:flex-end;margin-top:10px}
.quote .btn-light{border-color:var(--white)}

/* footer */
.footer{position:absolute;top:3420px;left:0;width:1200px;height:344px;background:var(--dark)}
.footer .grid{position:absolute;left:120px;right:120px;top:120px;display:flex;justify-content:space-between}
.footer h4{font-family:"Orbitron",sans-serif;font-size:16px;font-weight:800;color:var(--white);text-transform:uppercase;letter-spacing:2px;margin-bottom:20px}
.footer .info{font-size:14px;line-height:2;display:flex;flex-direction:column}
.footer .info span{display:flex;align-items:center;gap:10px}
.social{display:flex;gap:10px}
.social span{width:30px;height:30px;border-radius:50%;background:var(--brand-bright);display:block}
.copyright{position:absolute;top:280px;width:100%;text-align:center;font-size:13px;color:var(--muted)}
.to-top{position:absolute;right:20px;top:290px;width:36px;height:36px;border-radius:50%;background:var(--white);display:flex;align-items:center;justify-content:center}
</style>
</head>
<body>

<header class="hero">
  <div class="photo" role="img" aria-label="Steel storage tanks at a fabrication yard, in grey tones"></div>
  <nav class="nav">
    <div class="brand"><span class="mark"></span>Marlow Ridgeway</div>
    <ul class="menu">
      <li class="active">Home</li><li>About</li><li>Products</li><li>Services</li><li>Who we serve</li><li>Resources</li><li>Contact</li>
    </ul>
    <a class="btn btn-light">Request Quote
      <svg class="arrow" viewBox="0 0 14 8"><path d="M0 4h12M9 1l3 3-3 3" stroke="#fff" fill="none" stroke-width="1.4"/></svg></a>
  </nav>
  <div class="hero-copy">
    <p class="lead">Your Vision, Our Custom Quality</p>
    <h1 class="display">Fabrication Services</h1>
    <p class="phone">(555) 776-0125</p>
    <a class="btn btn-red">View this product
      <svg class="arrow" viewBox="0 0 14 8"><path d="M0 4h12M9 1l3 3-3 3" stroke="#fff" fill="none" stroke-width="1.4"/></svg></a>
  </div>
  <div class="slider"><span></span><span></span></div>
</header>

<section class="quality">
  <div class="heading">
    <p class="eyebrow">Quality Driven Fabrication</p>
    <h2 class="display">Quality Assurance<br>Guaranteed</h2>
  </div>
  <div class="photo pipes" role="img" aria-label="Stack of polished steel pipes"></div>
  <div class="content">
    <div class="badges"><span class="round"></span><span></span><span></span></div>
    <p>As experienced steel fabricators, we anticipate your needs and requirements from vision to production to delivery. Your steel fabrication projects are manufactured by proven business processes and some of the industry's top experts.</p>
    <div class="actions">
      <a class="btn btn-red">Products <svg class="arrow" viewBox="0 0 14 8"><path d="M0 4h12M9 1l3 3-3 3" stroke="#fff" fill="none" stroke-width="1.4"/></svg></a>
      <a class="btn btn-light">Services <svg class="arrow" viewBox="0 0 14 8"><path d="M0 4h12M9 1l3 3-3 3" stroke="#fff" fill="none" stroke-width="1.4"/></svg></a>
    </div>
  </div>
</section>

<div class="divider">
  <svg width="1200" height="42" viewBox="0 0 1200 42">
    <g fill="#55565c">
      <circle cx="40" cy="21" r="3"/><circle cx="120" cy="21" r="3"/><circle cx="200" cy="21" r="3"/><circle cx="280" cy="21" r="3"/><circle cx="360" cy="21" r="3"/><circle cx="440" cy="21" r="3"/><circle cx="520" cy="21" r="3"/><circle cx="680" cy="21" r="3"/><circle cx="760" cy="21" r="3"/><circle cx="840" cy="21" r="3"/><circle cx="920" cy="21" r="3"/><circle cx="1000" cy="21" r="3"/><circle cx="1080" cy="21" r="3"/><circle cx="1160" cy="21" r="3"/>
    </g>
    <path d="M586 0h28l-14 16z" fill="#2a2b31"/>
  </svg>
</div>

<section class="success">
  <div class="photo" role="img" aria-label="Welder at work with sparks, darkened"></div>
  <div class="copy">
    <p class="eyebrow">Built to specification, large or small</p>
    <h2 class="display">Success at any<br>size</h2>
    <div class="cols">
      <p>We deliver fabrication solutions from small-scale projects to our special steel oversized and overweight fabrication, processing and handling capabilities. Steel fabricators proudly serving the power generation sector.</p>
      <p>Treatment, water treatment, agriculture, chemical, food processing, mining, oil &amp; gas and heavy industry project sectors for nearly 50 years.</p>
    </div>
    <a class="btn btn-red">Who we serve <svg class="arrow" viewBox="0 0 14 8"><path d="M0 4h12M9 1l3 3-3 3" stroke="#fff" fill="none" stroke-width="1.4"/></svg></a>
  </div>
</section>

<section class="reviews">
  <div class="photo" role="img" aria-label="Row of cylindrical steel tanks on a support frame"></div>
  <div class="copy">
    <p class="eyebrow">Hear what our clients are saying</p>
    <h2 class="display">We may not be superheroes but our customers think we are.</h2>
    <div class="quote-mark">“</div>
    <blockquote>We will keep Marlow Ridgeway steel fabricators on our bidding list for vessels, tanks and stacks. Our catch tank constructed by them was of excellent workmanship and the exterior and interior met all of our expectations. We were impressed with the knowledgeable sales and engineering staff as well as their facilities. They worked well from the calculations for the foundation to the final tank design top quote.</blockquote>
    <div class="quote-mark close-mark">”</div>
    <div class="actions">
      <a class="btn btn-red">Case studies <svg class="arrow" viewBox="0 0 14 8"><path d="M0 4h12M9 1l3 3-3 3" stroke="#fff" fill="none" stroke-width="1.4"/></svg></a>
      <a class="btn btn-light">View clients <svg class="arrow" viewBox="0 0 14 8"><path d="M0 4h12M9 1l3 3-3 3" stroke="#fff" fill="none" stroke-width="1.4"/></svg></a>
    </div>
  </div>
</section>

<section class="quote">
  <p class="eyebrow">Start your project</p>
  <h2 class="display">Request a quote</h2>
  <div class="row">
    <div class="field"><label>First name:</label><div class="input">Enter your first name</div></div>
    <div class="field"><label>Last name:</label><div class="input">Enter your last name</div></div>
    <div class="field"><label>Company name:</label><div class="input">Enter your company name</div></div>
  </div>
  <div class="row">
    <div class="field"><label>Phone:</label><div class="input">Enter your phone number</div></div>
    <div class="field"><label>Email:</label><div class="input">Enter your email address</div></div>
  </div>
  <div class="row">
    <div class="field"><label>Description:</label><div class="input area">Describe your project</div></div>
  </div>
  <div class="submit">
    <a class="btn btn-light">Submit your request <svg class="arrow" viewBox="0 0 14 8"><path d="M0 4h12M9 1l3 3-3 3" stroke="#fff" fill="none" stroke-width="1.4"/></svg></a>
  </div>
</section>

<footer class="footer">
  <div class="grid">
    <div class="brand"><span class="mark"></span>Marlow Ridgeway</div>
    <div>
      <h4>Contact us</h4>
      <div class="info">
        <span><svg width="12" height="12" viewBox="0 0 12 12"><path d="M2 1l3 0 1 3-2 1a7 7 0 0 0 3 3l1-2 3 1v3c-6 0-10-4-10-10z" fill="#8e1a25"/></svg>(555) 776-0125</span>
        <span><svg width="12" height="10" viewBox="0 0 12 10"><rect x="0.5" y="0.5" width="11" height="9" fill="none" stroke="#8e1a25"/><path d="M1 1l5 4 5-4" fill="none" stroke="#8e1a25"/></svg>info@marlowridgeway.example</span>
      </div>
    </div>
    <div>
      <h4>Follow us</h4>
      <div class="social"><span></span><span></span><span></span></div>
    </div>
    <div>
      <h4>Get in touch</h4>
      <a class="btn btn-light" style="background:#fff;color:var(--ink)">Submit your request <svg class="arrow" viewBox="0 0 14 8"><path d="M0 4h12M9 1l3 3-3 3" stroke="#231F20" fill="none" stroke-width="1.4"/></svg></a>
    </div>
  </div>
  <p class="copyright">© 2018 Marlow Ridgeway. All Rights Reserved.</p>
  <div class="to-top"><svg width="12" height="12" viewBox="0 0 12 12"><path d="M2 8l4-4 4 4" fill="none" stroke="#231F20" stroke-width="1.6"/></svg></div>
</footer>

</body>
</html>
```